Popup-Fenster Design für Öffnungszeiten
Zielgruppe
Planung und Realisierung von individuellen Kaminen.
Aufgabenstellung
Für unsere Website www.lindenhaus-torvel.de benötigen wir ein Popup-Fenster für die Startseite. Da das Geschäft nicht jeden Tag und zu festen Zeit geöffnet hat, soll der Kunde direkt sehen können, wann das Geschäft das nächste Mal geöffnet hat. Das Popup-Fenster soll auffällig, jedoch nicht überladen und aufdringlich sein. Einen eigenen Entwurf (der mir nicht gefällt) habe ich hochgeladen. Vielleicht benötigt dieser nur noch einen Feinschliff!? Es muss nicht reckteckig sein, ich bin auch für runde oder ovale Formen offen. Der dort eingesetzte Text sollte als Platzhalter eingesetzt werden. Bei Fragen können Sie mir gerne eine Nachricht zukommen lassen.

```html
<!DOCTYPE html>
<html lang="de">
<head>
<meta charset="utf-8">
<title>Lindenhaus – Öffnungszeiten</title>
<link rel="stylesheet" href="https://fonts.googleapis.com/css2?family=Raleway:wght@200;300;400&family=Playfair+Display:ital,wght@0,700;1,700;1,900&family=Open+Sans:wght@400&display=swap">
<style>
  :root {
    --sidebar: #1b1a1a;
    --nav-text: #a9a6a1;
    --gold: #b39a5a;
    --gold-light: #d8c27a;
    --white: #ffffff;
    --ink: #0e0d0d;
    --text-dark: #2c2c2c;
    --frame: rgba(40, 40, 40, 0.85);
    --close: #e4141b;
  }
  * { margin: 0; padding: 0; box-sizing: border-box; }
  html, body { width: 1200px; height: 577px; overflow: hidden; background: var(--sidebar); }
  .page { position: relative; width: 1200px; height: 577px; }

  .sidebar { position: absolute; left: 0; top: 0; width: 264px; height: 577px; background: var(--sidebar); }
  .brand { position: absolute; left: 0; width: 264px; top: 62px; text-align: center; }
  .brand-mark { display: block; width: 46px; height: 46px; margin: 0 auto 12px; background: var(--gold); }
  .brand-name { font-family: "Raleway", sans-serif; font-weight: 400; font-size: 12.5px; letter-spacing: 3.6px; color: var(--gold); }
  .nav { position: absolute; left: 44px; top: 222px; list-style: none; }
  .nav li { font-family: "Raleway", sans-serif; font-weight: 300; font-size: 16px; color: var(--nav-text); height: 45.6px; }
  .legal { position: absolute; left: 44px; top: 539px; font-family: "Raleway", sans-serif; font-weight: 300; font-size: 10.5px; color: var(--nav-text); }

  .hero { position: absolute; left: 264px; top: 0; width: 936px; height: 577px;
    background:
      linear-gradient(172deg, transparent 0%, transparent 62%, rgba(196,170,140,0.0) 62%),
      linear-gradient(188deg, rgba(184,160,130,0.95) 0%, rgba(184,160,130,0.85) 8%, transparent 14%),
      linear-gradient(180deg, #6f86a6 0%, #a9b8cb 14%, #dde2e8 28%, #5c5a56 31%, #7b7263 36%, #6e6555 50%, #8c826f 64%, #c6bfb1 78%, #b29a7c 86%, #8d7458 100%); }
  .hero-title { position: absolute; left: 307px; top: 222px; font-family: "Raleway", sans-serif; font-weight: 200; font-size: 53px; letter-spacing: 1px; color: var(--white); white-space: nowrap; }
  .hero-sub { position: absolute; left: 540px; top: 285px; font-family: "Playfair Display", serif; font-style: italic; font-weight: 900; font-size: 35px; color: var(--white); white-space: nowrap; }
  .hero-cta { position: absolute; left: 619px; top: 510px; font-family: "Raleway", sans-serif; font-weight: 400; font-size: 10px; letter-spacing: 2.6px; color: #3c3a36; white-space: nowrap; }
  .hero-chevron { position: absolute; left: 724px; top: 533px; }

  .popup { position: absolute; left: 753px; top: 257px; width: 435px; height: 295px; }
  .popup svg.shape { position: absolute; left: 0; top: 0; }
  .popup-title { position: absolute; left: 16px; top: 70px; font-family: "Playfair Display", serif; font-weight: 700; font-size: 26px; color: var(--gold-light); }
  .popup-lead { position: absolute; left: 22px; top: 113px; font-family: "Open Sans", sans-serif; font-size: 12px; color: var(--white); }
  .hours { position: absolute; left: 45px; top: 131px; font-family: "Open Sans", sans-serif; font-size: 11px; line-height: 15px; color: var(--white); border-collapse: collapse; }
  .hours td { padding: 0 13px 0 0; }
  .popup-links { position: absolute; left: 23px; top: 245px; font-family: "Open Sans", sans-serif; font-size: 11.5px; line-height: 15px; color: var(--text-dark); width: 230px; }
  .close { position: absolute; left: 418px; top: -6px; width: 24px; height: 24px; border-radius: 50%; background: var(--close); color: var(--white); font-family: "Open Sans", sans-serif; font-size: 13px; line-height: 23px; text-align: center; }
</style>
</head>
<body>
<div class="page">
  <aside class="sidebar">
    <div class="brand">
      <span class="brand-mark"></span>
      <span class="brand-name">LINDENHAUS</span>
    </div>
    <ul class="nav">
      <li>ÜBER UNS</li>
      <li>KAMINÖFEN</li>
      <li>HOLZKAMINE</li>
      <li>GASKAMINE</li>
      <li>AUSSTELLUNG</li>
      <li>KONTAKT</li>
    </ul>
    <div class="legal">Impressum | Datenschutz</div>
  </aside>

  <section class="hero" role="img" aria-label="Hängender schwarzer Designkamin vor Panoramafenster mit Blick auf verschneite Berglandschaft unter Holzdecke"></section>
  <div class="hero-title">WILLKOMMEN IM LINDENHAUS</div>
  <div class="hero-sub">KAMINE FÜR JEDEN RAUM</div>
  <div class="hero-cta">Jetzt Beratungstermin vereinbaren</div>
  <svg class="hero-chevron" width="14" height="10" viewBox="0 0 14 10"><path d="M2 3 L7 8 L12 3" fill="none" stroke="#3c3a36" stroke-width="1.3"/></svg>

  <div class="popup">
    <svg class="shape" width="435" height="295" viewBox="0 0 435 295">
      <defs>
        <clipPath id="inner"><rect x="6" y="6" width="422" height="283" rx="8"/></clipPath>
        <radialGradient id="portrait" cx="0.62" cy="0.45" r="0.6">
          <stop offset="0" stop-color="#c9a08e"/>
          <stop offset="0.45" stop-color="#7a2a30"/>
          <stop offset="0.8" stop-color="#b7aca3"/>
          <stop offset="1" stop-color="#d8d3cd"/>
        </radialGradient>
      </defs>
      <rect x="0" y="0" width="435" height="295" rx="10" fill="var(--frame)"/>
      <rect x="6" y="6" width="422" height="283" rx="8" fill="var(--white)"/>
      <g clip-path="url(#inner)">
        <circle cx="336" cy="77" r="199" fill="var(--ink)"/>
        <circle cx="340" cy="72" r="191" fill="url(#portrait)" role="img" aria-label="Lächelnde Frau mit Sonnenbrille und Einkaufstaschen"/>
        <circle cx="117" cy="118" r="118" fill="var(--ink)"/>
      </g>
    </svg>
    <div class="popup-title">Öffnungszeiten</div>
    <div class="popup-lead">WIR HABEN FÜR SIE GEÖFFNET:</div>
    <table class="hours">
      <tr><td>Fr&nbsp; 17.01</td><td>14:00 - 17:00 Uhr</td></tr>
      <tr><td>Sa 18.01</td><td>10:00 - 13:00 Uhr</td></tr>
    </table>
    <div class="popup-links">Weitere Termine ansehen Indiviudellen Termin vereinbaren</div>
    <div class="close">X</div>
  </div>
</div>
</body>
</html>
```